VELOTRA Brisbane Tiling Service

My name is Milos Vrenbek i need a business card for a new company. We are wall and floor tilers based in Brisbane, our company is Velotra Brisbane Tiling Service.
We would like a logo from our website used on our cards. Our website is www.velotra-tiles.com.au

I would like my Facebook and Twitter accounts on my card.

Business

Colors
0692cd
3176b5
33a6d7
85cae6

```html
<!DOCTYPE html>
<html lang="en">
<head>
<meta charset="utf-8">
<title>Velotra Brisbane Tiling Service – Business Card</title>
<link rel="stylesheet" href="https://fonts.googleapis.com/css2?family=Open+Sans:wght@400&family=Arimo:wght@400;700&display=swap">
<style>
  :root {
    --stage: #e9e5dc;
    --navy: #0c1f45;
    --navy-light: #1d4079;
    --navy-band: #0b1c44;
    --blue: #0669ab;
    --blue-bright: #0692cd;
    --blue-mid: #3176b5;
    --blue-sky: #33a6d7;
    --blue-pale: #85cae6;
    --card-light: #f6f6f2;
    --ink: #1b2840;
    --white: #ffffff;
  }
  * { margin: 0; padding: 0; box-sizing: border-box; }
  html, body { width: 1200px; height: 720px; overflow: hidden; }
  body { background: var(--stage); position: relative; font-family: "Arimo", Arial, sans-serif; }

  .card { position: absolute; top: 232px; width: 537px; height: 307px; overflow: hidden; }

  /* Front */
  .card-front { left: 46px; background: radial-gradient(ellipse at 50% 40%, var(--navy-light) 0%, var(--navy) 70%); }
  .brand { position: absolute; display: flex; align-items: center; }
  .brand-square { flex: none; }
  .brand-text { font-family: "Open Sans", Arial, sans-serif; font-weight: 400; line-height: 1; }
  .brand-name { display: block; letter-spacing: 0.5px; }
  .brand-tagline { display: block; }

  .card-front .brand { left: 49px; top: 113px; }
  .card-front .brand-square { width: 95px; height: 95px; background: var(--white); margin-right: 8px; }
  .card-front .brand-text { color: var(--white); }
  .card-front .brand-name { font-size: 64px; margin-top: -18px; }
  .card-front .brand-tagline { font-size: 27px; margin-top: 4px; letter-spacing: 0.4px; }

  /* Back */
  .card-back { left: 600px; background: var(--card-light); }
  .card-back .brand { left: 93px; top: 36px; }
  .card-back .brand-square { width: 72px; height: 72px; background: linear-gradient(135deg, var(--blue-sky), var(--blue-mid)); margin-right: 8px; }
  .card-back .brand-text { color: var(--blue-sky); }
  .card-back .brand-name { font-size: 48px; margin-top: -10px; }
  .card-back .brand-tagline { font-size: 21px; margin-top: 2px; color: var(--blue-mid); }

  .holder { position: absolute; top: 128px; left: 0; width: 537px; text-align: center; }
  .holder-name { font-size: 20px; font-weight: 700; color: var(--ink); }
  .holder-title { font-size: 13px; color: var(--blue-mid); margin-top: 1px; }
  .rule { position: absolute; top: 153px; height: 1.5px; background: var(--navy-band); }
  .rule-left { left: 0; width: 172px; }
  .rule-right { left: 366px; width: 171px; }

  .swoosh { position: absolute; left: 0; top: 0; }

  .contacts { position: absolute; top: 210px; left: 97px; display: grid; grid-template-columns: 166px auto; row-gap: 8px; color: var(--white); font-size: 15px; }
  .contact { display: flex; align-items: center; gap: 5px; white-space: nowrap; }
  .contact-strong { font-weight: 700; }
  .contact svg { flex: none; }

  .website { position: absolute; left: 0; bottom: 0; width: 537px; height: 39px; background: var(--navy-band); color: var(--white); font-weight: 700; font-size: 18px; display: flex; align-items: center; justify-content: center; }
</style>
</head>
<body>

<section class="card card-front" aria-label="Card front">
  <div class="brand">
    <span class="brand-square"></span>
    <span class="brand-text">
      <span class="brand-name">velotra</span>
      <span class="brand-tagline">brisbane tiling service</span>
    </span>
  </div>
</section>

<section class="card card-back" aria-label="Card back">
  <div class="brand">
    <span class="brand-square"></span>
    <span class="brand-text">
      <span class="brand-name">velotra</span>
      <span class="brand-tagline">brisbane tiling service</span>
    </span>
  </div>

  <span class="rule rule-left"></span>
  <span class="rule rule-right"></span>
  <div class="holder">
    <div class="holder-name">Milos Vrenbek</div>
    <div class="holder-title">Chief Executive Officer</div>
  </div>

  <svg class="swoosh" width="537" height="307" viewBox="0 0 537 307" aria-hidden="true">
    <path d="M0,192 Q250,168 537,182 L537,196 Q270,182 0,212 Z" fill="var(--navy-band)"/>
    <path d="M0,212 Q270,182 537,196 L537,268 L0,268 Z" fill="var(--blue)"/>
  </svg>

  <div class="contacts">
    <span class="contact contact-strong">
      <svg width="15" height="15" viewBox="0 0 16 16"><circle cx="8" cy="8" r="7" fill="none" stroke="#fff" stroke-width="1.4"/><path d="M5.2 4.2l1.4 1.6-.7 1a5 5 0 0 0 2.3 2.3l1-.7 1.6 1.4-.8 1.2C7.6 11 5 8.4 4 5z" fill="#fff"/></svg>
      07-5550-1842
    </span>
    <span class="contact contact-strong">
      <svg width="15" height="15" viewBox="0 0 16 16"><circle cx="8" cy="8" r="7" fill="none" stroke="#fff" stroke-width="1.4"/><rect x="4.3" y="5.3" width="7.4" height="5.4" fill="#fff"/><path d="M4.3 5.3L8 8.3l3.7-3" fill="none" stroke="var(--blue)" stroke-width="0.9"/></svg>
      hello@velotra-tiles.com.au
    </span>
    <span class="contact">
      <svg width="15" height="15" viewBox="0 0 16 16"><circle cx="8" cy="8" r="7" fill="none" stroke="#fff" stroke-width="1.4"/></svg>
      fb.com/velotra
    </span>
    <span class="contact">
      <svg width="15" height="15" viewBox="0 0 16 16"><circle cx="8" cy="8" r="7" fill="none" stroke="#fff" stroke-width="1.4"/></svg>
      @velotra
    </span>
  </div>

  <div class="website">www.velotra-tiles.com.au</div>
</section>

</body>
</html>
```